Brivet Networks, Inc. Website redesign

Revamp the website, it is old and outdated. www.brivetnetworksinc.com

Target Market(s)

Information Technology Consulting and Staffing

Coding

Coded - Design and coding required

Number of Pages Required

5+ page

Colors

Designer to choose colors to be used in the design.

Requirements
Must have
• Outlined text boxes just like from the Hollis.us site. A clean look

```html
<!DOCTYPE html>
<html lang="en">
<head>
<meta charset="utf-8">
<title>Brivet Networks, Inc.</title>
<link rel="stylesheet" href="https://fonts.googleapis.com/css2?family=Michroma&family=Jost:wght@400;500&display=swap">
<style>
:root{
  --red:#a31b32;
  --ink:#1c1c1c;
  --text:#3a3a3a;
  --muted:#6b6b6b;
  --line:#d7d7d7;
  --soft:#f2f2f2;
  --dark:#333333;
  --white:#ffffff;
}
*{box-sizing:border-box;margin:0;padding:0}
html,body{width:1200px;height:2874px;overflow:hidden}
body{position:relative;background:var(--white);font-family:"Jost",sans-serif;color:var(--text)}
.abs{position:absolute}
.accent{color:var(--red)}

/* header */
.site-header{left:0;top:0;width:1200px;height:102px;background:var(--white)}
.brand{left:141px;top:30px;display:flex;align-items:center;gap:10px;font-size:30px;font-weight:500;color:var(--ink);letter-spacing:.5px;white-space:nowrap}
.brand-mark{width:26px;height:26px;background:var(--red);flex:none}
.btn-touch{left:927px;top:19px;width:131px;height:30px;border:2px solid var(--red);font-family:"Michroma",sans-serif;font-size:10px;letter-spacing:.5px;color:var(--ink);display:flex;align-items:center;justify-content:center;white-space:nowrap}
.main-nav{right:142px;top:54px;display:flex;gap:22px;align-items:flex-start;font-family:"Michroma",sans-serif;font-size:9.5px;color:var(--ink);white-space:nowrap}
.main-nav span{padding-top:18px}
.main-nav .current{background:var(--red);color:var(--white);padding:18px 10px 20px;clip-path:polygon(0 0,100% 0,100% 72%,50% 100%,0 72%)}

/* hero */
.hero{left:0;top:102px;width:1200px;height:458px;background:linear-gradient(90deg,#2f4470 0%,#6d7891 30%,#c6c9cf 55%,#e4e4e4 75%,#d6d8dc 100%)}
.hero-copy{right:147px;top:228px;text-align:right;color:var(--ink);white-space:nowrap}
.hero-copy h1{font-family:"Michroma",sans-serif;font-size:31px;font-weight:400;letter-spacing:.5px;margin-bottom:8px;line-height:40px}
.hero-copy p{font-size:27px;line-height:36px}
.btn-red{background:var(--red);color:var(--white);display:flex;align-items:center;justify-content:center;white-space:nowrap}
.hero-cta{right:147px;top:399px;width:176px;height:28px;font-family:"Michroma",sans-serif;font-size:11px;letter-spacing:.5px}

/* about */
.about{left:0;top:560px;width:1200px;height:504px;background:var(--soft)}
.section-title{width:1200px;left:0;text-align:center;font-family:"Michroma",sans-serif;font-size:24px;color:var(--ink);letter-spacing:1px;font-weight:400;white-space:nowrap}
.lead{left:150px;width:900px;text-align:center;font-size:17.5px;line-height:30px;color:var(--ink)}
.service{top:785px;width:219px;height:232px;border:1px solid var(--red);background:var(--soft);text-align:center;padding-top:28px}
.service .icon{height:58px;display:flex;align-items:center;justify-content:center;margin-bottom:12px}
.service h3{font-size:16.5px;font-weight:500;line-height:21px;color:var(--ink);margin-bottom:10px}
.service p{font-size:13px;line-height:20px;color:var(--text);padding:0 8px}

/* news */
.news-card{top:1203px;width:285px;height:395px;border:1px solid var(--line);background:var(--white)}
.news-image{width:283px;height:210px}
.news-body{padding:24px 15px 0}
.news-body h3{font-size:16px;font-weight:500;color:var(--ink);margin-bottom:16px}
.news-body p{font-size:13.5px;line-height:18px;color:var(--text);margin-bottom:20px}
.news-body a{font-size:13.5px;color:var(--text);text-decoration:underline}
.slider-arrow{top:1388px;width:25px;height:25px;border-radius:50%}
.view-all{left:537px;top:1619px;width:126px;height:28px;font-family:"Michroma",sans-serif;font-size:11px;letter-spacing:.5px}

/* strategy */
.strategy{left:141px;top:1719px;width:918px;height:283px;border:1px solid var(--line)}

/* inquiry */
.site-footer{left:0;top:2441px;width:1200px;height:433px;background:var(--dark)}
.inquiry{left:268px;top:2081px;width:664px;height:465px;background:var(--white);border-radius:0 0 4px 0}
.inquiry-fold{left:268px;top:2510px}
.field{height:35px;border:1px solid var(--line);font-size:13px;color:var(--muted);padding:8px 14px;background:var(--white)}
.submit{left:540px;top:2468px;width:120px;height:35px;font-size:16px}

/* footer */
.foot-head{top:2605px;font-size:18px;color:var(--white);font-weight:400}
.foot-rule{top:2637px;width:52px;height:1px;background:var(--red)}
.quick-links{left:160px;top:2655px;list-style:none;font-size:13.5px;color:var(--white);line-height:28px}
.contact-list{left:310px;top:2657px;font-size:12.5px;color:var(--white);line-height:20px}
.contact-list .row{display:flex;gap:10px;margin-bottom:8px}
.contact-list strong{font-weight:400;font-size:15px}
.map{left:556px;top:2657px;width:219px;height:128px;background:linear-gradient(135deg,#eceae6,#dcdad5)}
.foot-brand{left:842px;top:2660px;display:flex;align-items:center;gap:10px;font-size:30px;font-weight:500;color:var(--white);white-space:nowrap}
.foot-brand .brand-mark{background:var(--white)}
.follow{left:842px;top:2728px;display:flex;align-items:center;gap:12px;font-size:18px;color:var(--white);white-space:nowrap}
.social{width:27px;height:27px;border-radius:50%}
.copyright{left:0;top:2830px;width:1200px;text-align:center;font-size:13px;color:var(--white)}
</style>
</head>
<body>

<header class="abs site-header">
  <div class="abs brand"><span class="brand-mark"></span>Brivet Networks</div>
  <div class="abs btn-touch">GET IN TOUCH</div>
  <nav class="abs main-nav">
    <span class="current">HOME</span>
    <span>ABOUT US</span><span>SERVICES</span><span>STRATEGY</span><span>LATEST NEWS</span><span>CONTACT US</span>
  </nav>
</header>

<section class="abs hero" role="img" aria-label="Two businessmen in suits reviewing a tablet in a bright office"></section>
<div class="abs hero-copy">
  <h1>We Provide Our Clients</h1>
  <p>With Cutting-Edge Technologies And<br>The Know-How To Apply Them To<br>Their Individual Business Models.</p>
</div>
<div class="abs btn-red hero-cta">CONTACT US TODAY</div>

<section class="abs about"></section>
<h2 class="abs section-title" style="top:638px">ABOUT BRIVET <span class="accent">NETWORKS</span></h2>
<p class="abs lead" style="top:692px">Brivet Networks, Inc. is an 8(a) innovative and rapidly growing full-service IT consulting firm. We provide our clients with cutting-edge technologies and the know-how to apply them to their individual business models…{+}</p>

<div class="abs service" style="left:141px">
  <div class="icon"><svg width="42" height="52" viewBox="0 0 42 52" fill="none" stroke="var(--red)" stroke-width="2"><rect x="2" y="2" width="38" height="48" rx="3"/><circle cx="21" cy="23" r="11"/><circle cx="21" cy="23" r="3"/><path d="M8 42h26"/></svg></div>
  <h3>HARDWARE /<br>SOFTWARE SALES</h3>
  <p>Lorem ipsum dolor sit amet says of consectetuer adipiscii elit, sed diam nonummy nibh euismod</p>
</div>
<div class="abs service" style="left:374px">
  <div class="icon"><svg width="42" height="56" viewBox="0 0 42 56" fill="none" stroke="var(--red)" stroke-width="2"><rect x="2" y="5" width="38" height="49" rx="3"/><rect x="14" y="1" width="14" height="7"/><path d="M9 18h5M19 18h14M9 28h5M19 28h14M9 38h5M19 38h14M9 47h5M19 47h14"/></svg></div>
  <h3>TECHNOLOGY<br>ASSESSMENT</h3>
  <p>Lorem ipsum dolor sit amet says of consectetuer adipiscii elit, sed diam nonummy nibh euismod</p>
</div>
<div class="abs service" style="left:607px">
  <div class="icon"><svg width="62" height="56" viewBox="0 0 62 56" fill="none" stroke="var(--red)" stroke-width="2"><rect x="2" y="10" width="46" height="32"/><path d="M18 42v8M32 42v8M12 52h26M8 18h10v8H8zM24 20h18M24 28h18M8 34h34"/><circle cx="52" cy="9" r="6"/><circle cx="52" cy="9" r="2"/></svg></div>
  <h3>TECHNOLOGY<br>CONSULTING</h3>
  <p>Lorem ipsum dolor sit amet says of consectetuer adipiscii elit, sed diam nonummy nibh euismod</p>
</div>
<div class="abs service" style="left:840px">
  <div class="icon"><svg width="50" height="52" viewBox="0 0 50 52" fill="none" stroke="var(--red)" stroke-width="2"><path d="M14 2h26v48H14z"/><rect x="2" y="20" width="30" height="26"/><path d="M12 20v-5h10v5M2 30h30M14 28v5h6v-5"/></svg></div>
  <h3>PROFESSIONAL<br>SERVICES</h3>
  <p>Lorem ipsum dolor sit amet says of consectetuer adipiscii elit, sed diam nonummy nibh euismod</p>
</div>

<h2 class="abs section-title" style="top:1139px">LATEST <span class="accent">NEWS</span></h2>

<svg class="abs slider-arrow" style="left:99px" viewBox="0 0 25 25"><circle cx="12.5" cy="12.5" r="12" fill="#fff" stroke="#ddd"/><path d="M17 12.5H8m3-3-3 3 3 3" fill="none" stroke="#888" stroke-width="1.3"/></svg>
<svg class="abs slider-arrow" style="left:1075px" viewBox="0 0 25 25"><circle cx="12.5" cy="12.5" r="12" fill="#555"/><path d="M8 12.5h9m-3-3 3 3-3 3" fill="none" stroke="#fff" stroke-width="1.3"/></svg>

<article class="abs news-card" style="left:152px">
  <div class="news-image" role="img" aria-label="Engineers in a blue-lit network operations center" style="background:linear-gradient(160deg,#1b2c4a,#3b5f8e 60%,#7fa6cf)"></div>
  <div class="news-body"><h3>LOREM IPSUM DOLOR SIT AMET</h3><p>Lorem ipsum dolor sit amet, consectetuer adipiscii elit, sed diam nonummy nibh euismod tincidunt ut..{+}</p><a>READ MORE</a></div>
</article>
<article class="abs news-card" style="left:458px">
  <div class="news-image" role="img" aria-label="Two technicians with a laptop in a server room" style="background:linear-gradient(160deg,#2b3340,#5c6675 55%,#9aa3ad)"></div>
  <div class="news-body"><h3>LOREM IPSUM DOLOR SIT AMET</h3><p>Lorem ipsum dolor sit amet, consectetuer adipiscii elit, sed diam nonummy nibh euismod tincidunt ut..{+}</p><a>READ MORE</a></div>
</article>
<article class="abs news-card" style="left:763px">
  <div class="news-image" role="img" aria-label="Cloud computing concept with connected computers" style="background:linear-gradient(180deg,#1d5e8e,#5ea8d3 45%,#d9ecf6)"></div>
  <div class="news-body"><h3>LOREM IPSUM DOLOR SIT AMET</h3><p>Lorem ipsum dolor sit amet, consectetuer adipiscii elit, sed diam nonummy nibh euismod tincidunt ut..{+}</p><a>READ MORE</a></div>
</article>
<div class="abs btn-red view-all">VIEW ALL</div>

<section class="abs strategy"></section>
<h2 class="abs section-title" style="top:1786px">OUR <span class="accent">STRATEGY</span></h2>
<p class="abs lead" style="top:1840px;font-size:18px;line-height:31px">Civilian and Federal agencies are facing increased demands driven by the changing economic environment and shifts in the way products and services are sold and delivered. These factors have created an imperative to leverage new and innovative technology solution architectures…{+}</p>

<footer class="abs site-footer"></footer>

<section class="abs inquiry"></section>
<svg class="abs inquiry-fold" width="36" height="36" viewBox="0 0 36 36"><path d="M0 0H36V36Z" fill="var(--red)"/><path d="M0 0L36 36H0Z" fill="var(--dark)"/></svg>
<h2 class="abs section-title" style="top:2143px">QUICK <span class="accent">INQUIRY</span></h2>
<p class="abs lead" style="top:2191px;font-size:14.5px">Lorem Ipsum is simply dummy text of the printing and typesetting industry.</p>
<div class="abs field" style="left:325px;top:2254px;width:268px">First Name</div>
<div class="abs field" style="left:607px;top:2254px;width:268px">Last Name</div>
<div class="abs field" style="left:325px;top:2303px;width:268px">Phone</div>
<div class="abs field" style="left:607px;top:2303px;width:268px">Email</div>
<div class="abs field" style="left:325px;top:2354px;width:550px;height:84px">Message</div>
<div class="abs btn-red submit">SUBMIT</div>

<h4 class="abs foot-head" style="left:143px">Quick Links</h4>
<div class="abs foot-rule" style="left:143px"></div>
<ul class="abs quick-links"><li>HOME</li><li>ABOUT US</li><li>SERVICES</li><li>STRATEGY</li><li>LATEST NEWS</li><li>CONTACT US</li></ul>

<h4 class="abs foot-head" style="left:310px">Contact Details</h4>
<div class="abs foot-rule" style="left:310px"></div>
<div class="abs contact-list">
  <div class="row"><svg width="13" height="17" viewBox="0 0 13 17"><path d="M6.5 0A6.5 6.5 0 0 0 0 6.5C0 11 6.5 17 6.5 17S13 11 13 6.5A6.5 6.5 0 0 0 6.5 0Z" fill="var(--red)"/><circle cx="6.5" cy="6.5" r="2.4" fill="var(--dark)"/></svg><div><strong>BRIVET NETWORKS</strong><br>2280 Lindenfield Ct,<br>Ashvale, MD 20911, USA</div></div>
  <div class="row"><svg width="13" height="13" viewBox="0 0 13 13"><path d="M3 0l2 3-1.5 1.5a8 8 0 0 0 5 5L10 8l3 2-1.5 2.5C6 13 0 7 .5 1.5Z" fill="var(--red)"/></svg><span style="font-size:14px">301-555-0187</span></div>
  <div class="row"><svg width="13" height="10" viewBox="0 0 13 10"><rect width="13" height="10" fill="var(--red)"/><path d="M0 0l6.5 5L13 0" fill="none" stroke="var(--dark)"/></svg><span>info@brivetnetworksinc.com</span></div>
</div>

<h4 class="abs foot-head" style="left:556px">Contact Details</h4>
<div class="abs foot-rule" style="left:556px"></div>
<div class="abs map" role="img" aria-label="Street map showing the office location"></div>

<div class="abs foot-brand"><span class="brand-mark"></span>Brivet Networks</div>
<div class="abs follow">Follow Us On <span class="social" style="background:#1877f2;margin-left:8px"></span><span class="social" style="background:#1da1e0"></span></div>

<p class="abs copyright">Copyright © 2019 Brivet Networks. All Rights Reserved.</p>

</body>
</html>
```